Billboard Design for Modern Dispensary

Hello!
We need a eye-catching 12' x 24' billboard designed for a very successful, modern cannabis dispensary on the Oregon coast, United States. Because of rules, we cannot have any marijuana leafs or other cannabis related images (flower, joints, smoke, etc). We can use the words "Shop" or "Dispensary" - we cannot use the words "cannabis", "marijuana".

Some ideas we had are 3 words stacked on left or center of billboard - maybe across bottom we have horizontal logo and the following words - “North of harbor in Seagull Cove”
Another idea is to have a small bubble in bottom/top corner with image of our dog (face only) - with some words around it - like "BONUS Shop Dog" or "Cute Shop Dog" or "Best Shop Dog" or "Friendly Staff"

here's some 3 word examples:
ENJOY
YOUR
TRIP

or

FEEL
GOOD
JUST
AHEAD

or

GOOD
VIBES
ONLY

or

GOOD
TIMES
CHILL
VIBES

I have attached our logo. I have also included a stacked logo version (vertical, not horizontal). the formats are .EPS and .PDF - the logos were created in Affinity Design 2.x.

Our website is coralnook.net if you want to see more images, etc about our dispensary.

Artwork Requirements:
The billboard is 12' tall x 25' wide
The artwork needs to be 1”=1’ @ 300dpi
Please add 6” of bleed all around so your total artwork is 13”x26”
Final deliverable should be .Ai file.

Font styles to use
Sans Serif

Colors
0054AA
0677BA
7BADD7
CADEEF
E8F1F8

Requirements
Nice to have
• See the project description - we included some ideas to consider.
Should not have
• No cannabis images, like flower, cannabis leaves, paraphenlia, cartridges, joints, etc.

```html
<!DOCTYPE html>
<html lang="en">
<head>
<meta charset="utf-8">
<title>Coral Nook Billboard</title>
<link href="https://fonts.googleapis.com/css2?family=Luckiest+Guy&family=Montserrat:wght@500;700;800&display=swap" rel="stylesheet">
<style>
  :root {
    --page: #e8f1f8;
    --sky: #3d97db;
    --sky-light: #62aee6;
    --sky-deep: #0677ba;
    --navy: #0b2a55;
    --ink: #0d0d0d;
    --white: #ffffff;
    --brand: #3d8fd1;
  }
  * { margin: 0; padding: 0; box-sizing: border-box; }
  html, body {
    width: 1200px; height: 900px; overflow: hidden;
    background: var(--page);
  }
  .billboard {
    position: absolute; left: 40px; top: 170px;
    width: 1120px; height: 560px;
    overflow: hidden;
    background: radial-gradient(ellipse at 52% 45%, var(--sky-light) 0%, var(--sky) 55%, #3590d6 100%);
    box-shadow: 0 10px 30px rgba(11, 42, 85, 0.2);
  }
  .corner-panel { position: absolute; left: 0; top: 0; }
  .brand {
    position: absolute; left: 40px; top: 28px;
    display: flex; align-items: center; gap: 12px;
  }
  .brand-dot {
    width: 70px; height: 70px; border-radius: 50%;
    background: var(--brand);
  }
  .brand-text { display: flex; flex-direction: column; }
  .brand-name {
    font-family: "Montserrat", sans-serif; font-weight: 500;
    font-size: 34px; color: var(--brand); letter-spacing: -0.5px; line-height: 1;
  }
  .brand-place {
    margin-top: 8px;
    font-family: "Montserrat", sans-serif; font-weight: 500;
    font-size: 11px; letter-spacing: 5px; color: var(--navy);
    display: flex; align-items: center; gap: 10px;
  }
  .brand-place::before, .brand-place::after {
    content: ""; width: 28px; height: 1px; background: var(--navy);
  }
  .headline {
    position: absolute; left: 250px; top: 88px; width: 660px;
    text-align: center;
    font-family: "Luckiest Guy", "Arial Black", sans-serif;
    font-weight: 400;
    color: var(--white);
    line-height: 0.9;
    -webkit-text-stroke: 12px var(--sky-deep);
    paint-order: stroke fill;
    text-shadow: 5px 7px 0 var(--navy);
  }
  .headline span { display: block; }
  .headline .word-best { font-size: 104px; }
  .headline .word-dispensary { font-size: 104px; letter-spacing: -3px; }
  .headline .word-period { font-size: 104px; }
  .location {
    position: absolute; left: 0; right: 0; top: 424px;
    display: flex; justify-content: center; align-items: center; gap: 20px;
    font-family: "Montserrat", sans-serif; font-weight: 800;
    font-size: 29px; color: var(--white); letter-spacing: 0.5px;
  }
  .location::before, .location::after {
    content: ""; width: 72px; height: 2px; background: var(--white);
  }
  .contact-bar {
    position: absolute; left: 0; right: 0; bottom: 0; height: 84px;
    display: flex;
  }
  .contact-phone {
    width: 580px; background: var(--white);
    display: flex; align-items: center; justify-content: center;
    font-family: "Montserrat", sans-serif; font-weight: 800;
    font-size: 62px; color: var(--brand); letter-spacing: -1px;
  }
  .contact-web {
    flex: 1; background: var(--ink);
    display: flex; align-items: center; justify-content: center;
    font-family: "Montserrat", sans-serif; font-weight: 800;
    font-size: 58px; color: var(--white); letter-spacing: -1px;
  }
</style>
</head>
<body>
  <main class="billboard">
    <svg class="corner-panel" width="480" height="170" viewBox="0 0 480 170" aria-hidden="true">
      <polygon points="0,0 480,0 290,150 0,110" fill="#ffffff"/>
    </svg>

    <div class="brand">
      <div class="brand-dot"></div>
      <div class="brand-text">
        <span class="brand-name">CORAL NOOK</span>
        <span class="brand-place">SEAGULL COVE</span>
      </div>
    </div>

    <h1 class="headline">
      <span class="word-best">BEST</span>
      <span class="word-dispensary">DISPENSARY</span>
      <span class="word-period">PERIOD</span>
    </h1>

    <p class="location">NORTH OF HARBOR IN SEAGULL COVE</p>

    <div class="contact-bar">
      <div class="contact-phone">541-555-0142</div>
      <div class="contact-web">coralnook.net</div>
    </div>
  </main>
</body>
</html>
```